Capability Statement Brochure - Corporate

We need to provide our corporate clients with an elegant, professional and well designed capability statement that not only details what our business can offer, but reflects our professionalism with relevant technical photos. I am thinking two pages A 4 pdf will be suitable if the text can fit without looking crowded but happy to extend to 3 or 4 pages if needed . Colours and details can be taken from our website www.quorintech.com.au Some photos have been attached however if we need more professional stock photos I am happy to use them if needed. This project needs to convince potential clients we are the best in industry and our capability is extensive. Please help us relay this to our customers. Thank you,.

Target Market(s)

Corporate, Government, Education, Defence, Healthcare

Industry/Entity Type

Audio Visual Integration

Colors
0054AA
0677BA
7BADD7
CADEEF
E8F1F8

Requirements
Must have
• Style, look classy, sophisticated and technical
Nice to have
• Quorin Tech colours, Logo, website and email and include the PRISM LED Logo
Should not have
• Messy, too much clutter, not easy to read.

```html
<!DOCTYPE html>
<html lang="en">
<head>
<meta charset="utf-8">
<title>Quorin Tech Capability Statement</title>
<link rel="stylesheet" href="https://fonts.googleapis.com/css2?family=Manrope:wght@400;500;600&family=Inter:wght@400;500&display=swap">
<style>
:root{
  --board:#ffffff;
  --ink-dark:#0d1219;
  --navy:#15365c;
  --night-a:#0c1118;
  --night-b:#152238;
  --accent:#5cc3ee;
  --muted:#8c96a3;
  --grey:#9aa1a8;
  --paper:#ffffff;
  --body:#2c2f33;
  --rule:#3d5f86;
}
*{margin:0;padding:0;box-sizing:border-box}
html,body{width:1200px;height:849px;overflow:hidden;background:var(--board)}
body{position:relative;font-family:'Inter',sans-serif}
.page{position:absolute;width:240px;height:240px;overflow:hidden}
.page > *{position:absolute}
.dark{background:linear-gradient(160deg,var(--night-a) 0%,var(--night-b) 55%,var(--night-a) 100%);color:var(--muted)}
.light{background:linear-gradient(90deg,var(--paper) 0%,var(--paper) 80%,#d9dadb 100%);color:var(--body)}
.photo{background:linear-gradient(180deg,#bdbdbd,#5e5e5e 60%,#3a3a3a)}
.photo.desk{background:linear-gradient(180deg,#d3d3d3,#6a6a6a 70%,#464646)}
.photo.console{background:linear-gradient(135deg,#4a4a4a,#1f1f1f 45%,#6a6a6a 80%,#2a2a2a)}
.head{font-family:'Manrope',sans-serif;font-weight:500;font-size:7px;line-height:1.1;color:var(--grey)}
.head b{font-weight:500;color:var(--accent)}
.light .head{color:#3a3d42}
.copy{font-size:2.7px;line-height:1.55;text-align:justify}
.copy p+p{margin-top:2.4px}
.light .copy{color:#3a3d42}
.footer{font-size:2.6px;letter-spacing:.2px;color:var(--grey)}
.wordmark{font-family:'Manrope',sans-serif;font-weight:600;color:#c9ced4;font-size:6px}
.rule{height:.5px;background:var(--rule)}
.display{font-family:'Manrope',sans-serif;font-weight:400;font-size:13px;line-height:1.1;color:#d5d9de;text-align:center}
.cap-list{list-style:none;font-size:3px;line-height:1.6}
.cap-list li{padding-left:5px;position:relative}
.cap-list li::before{content:"";position:absolute;left:0;top:1px;width:2px;height:2.4px;background:#2c2f33}
.market-list{list-style:none;font-size:4.6px;line-height:1.55;color:#a9b1bb}
</style>
</head>
<body>

<!-- Front cover -->
<section class="page cover" style="left:212px;top:51px;background:var(--navy)">
  <div style="left:0;top:0;width:240px;height:45px;background:var(--ink-dark)"></div>
  <div class="wordmark" style="left:30px;top:18px">quorin tech</div>
  <div class="photo" role="img" aria-label="Boardroom table with rows of mesh office chairs" style="left:0;top:44px;width:240px;height:82px"></div>
  <h1 class="display" style="left:0;top:134px;width:240px;color:#d0d6de">Connecting People<br>With Technology</h1>
  <p style="right:20px;top:183px;font-size:6px;line-height:1.05;text-align:right;color:var(--accent);font-family:'Inter',sans-serif">“ A leading Australian<br>Audiovisual Integration<br>Specialist ”</p>
  <div class="rule" style="left:136px;top:209px;width:84px;background:#0c1a2c"></div>
  <p class="footer" style="right:20px;top:216px;color:#0c1a2c">www.quorintech.com.au</p>
</section>

<!-- Spread 1 left: company overview -->
<section class="page light" style="left:510px;top:51px">
  <div class="wordmark" style="left:24px;top:19px;color:#55585c">quorin tech</div>
  <h2 class="head" style="left:23px;top:47px"><b>Company</b><br>Overview</h2>
  <div class="copy" style="left:77px;top:25px;width:141px">
    <p style="color:var(--accent);font-weight:500;font-size:3px">Quorin Tech Systems (QTS)</p>
    <p>is a leading Australian audiovisual integration specialist delivering advanced AV, unified communications, collaboration environments, and large-scale digital display systems across Australia.</p>
    <p>With more than 26 years of industry experience, QTS provides end-to-end services including system design, engineering, installation, commissioning, and long-term technical support. Our solutions enable organisations to communicate, collaborate, and share information effectively across boardrooms, control centres, training environments, operational facilities, and large public spaces.</p>
    <p>QTS works across a broad range of sectors including healthcare, corporate enterprise, government, defence, mining and resources, and education. Our team combines deep technical expertise with a strong understanding of operational environments where reliability, security, and ease of use are essential.</p>
  </div>
  <div class="photo desk" role="img" aria-label="Training room with rows of desks and computer monitors" style="left:0;top:111px;width:240px;height:43px"></div>
  <h2 class="head" style="left:27px;top:163px;color:#3a3d42"><b>Core</b> Capabilities</h2>
  <ul class="cap-list" style="left:27px;top:178px;width:82px">
    <li>AV System Design &amp; Engineering</li>
    <li>Unified Communications &amp; Collaboration Systems</li>
    <li>LED Video Walls &amp; Large Format Displays</li>
    <li>Control Rooms &amp; Operations Centres</li>
    <li>Boardrooms &amp; Executive Meeting Spaces</li>
  </ul>
  <div style="left:121px;top:176px;width:.5px;height:34px;background:#3a3d42"></div>
  <ul class="cap-list" style="left:136px;top:178px;width:90px">
    <li>Education &amp; Training Environments</li>
    <li>Digital Signage &amp; Information Display Networks</li>
    <li>AV over IP &amp; Networked Media Systems</li>
    <li>System Programming, Automation &amp; Control</li>
    <li>Ongoing Service, Maintenance &amp; Technical Support</li>
  </ul>
  <p class="footer" style="left:0;width:240px;text-align:center;top:219px;color:#3a3d42">www.quorintech.com.au</p>
</section>

<!-- Spread 1 right: LED, markets, healthcare -->
<section class="page dark" style="left:750px;top:51px">
  <h2 class="head" style="left:23px;top:25px"><b>LED Video</b><br>Wall Expertise</h2>
  <div class="wordmark" style="left:168px;top:25px;color:#9aa1a8">PRISM LED</div>
  <div class="copy" style="left:23px;top:54px;width:193px;color:#5d6774">
    <p>Quorin Tech Systems has extensive experience designing and installing direct-view LED video walls for corporate environments, education facilities, public venues, and large presentation spaces.</p>
    <p>Our proprietary PRISM LED video wall solutions provide exceptional brightness, durability, and reliability for high-impact display environments such as school halls, gymnasiums, corporate auditoriums, and public venues.</p>
    <p>QTS provides complete LED video wall solutions including structural design, engineering certification, installation, commissioning, and ongoing support.</p>
  </div>
  <div class="rule" style="left:23px;top:106px;width:193px"></div>
  <h2 class="head" style="left:23px;top:125px"><b>Markets</b><br>Served</h2>
  <ul class="market-list" style="left:77px;top:122px">
    <li>Healthcare</li><li>Corporate &amp; Enterprise</li><li>Government</li><li>Defence</li>
  </ul>
  <ul class="market-list" style="left:157px;top:122px">
    <li>Mining &amp; Resources</li><li>Education</li><li>Public Venues &amp; Event</li><li>Spaces</li>
  </ul>
  <div class="rule" style="left:23px;top:158px;width:193px"></div>
  <h2 class="head" style="left:23px;top:182px"><b>Healthcare</b><br>Experience</h2>
  <div class="copy" style="left:77px;top:174px;width:141px;color:#5d6774">
    <p>QTS has extensive experience delivering audiovisual solutions within major healthcare environments including clinical communication systems, specialist consultation rooms, training facilities, and hospital-wide digital signage networks.</p>
    <p>For over 20 years QTS has supported Harbourview General Hospital with the design, implementation, and support of audiovisual infrastructure across departments including ICU, Emergency, Cardiology, Radiology, and Allied Health.</p>
  </div>
  <p class="footer" style="left:0;width:240px;text-align:center;top:219px;color:#5d6774">quorin tech</p>
</section>

<!-- Spread 2 left: sectors -->
<section class="page dark" style="left:92px;top:305px">
  <h2 class="head" style="left:23px;top:25px"><b>Corporate</b><br>&amp; Enterprise</h2>
  <div class="copy" style="left:84px;top:25px;width:134px;color:#5d6774">
    <p>QTS delivers modern collaboration environments that enable organisations to connect teams across offices, remote staff, and global partners. Solutions include boardrooms, hybrid meeting rooms, training facilities, corporate digital signage networks, and executive collaboration spaces.</p>
  </div>
  <div class="photo" role="img" aria-label="Meeting room with white table, mesh chairs and a potted plant" style="left:0;top:59px;width:240px;height:43px"></div>
  <h2 class="head" style="left:23px;top:120px"><b>Government</b><br>&amp; Defence</h2>
  <div class="copy" style="left:84px;top:120px;width:134px;color:#5d6774">
    <p>QTS supports government departments and defence organisations with reliable and secure audiovisual systems designed for operational environments including command centres, training facilities, situation rooms, and secure conferencing spaces.</p>
  </div>
  <h2 class="head" style="left:23px;top:159px"><b>Mining &amp;</b><br>Resources</h2>
  <div class="copy" style="left:23px;top:182px;width:81px;color:#5d6774">
    <p>QTS provides robust AV systems designed for industrial and remote environments including operations centres, training rooms, induction facilities, and remote collaboration systems supporting mining and energy sector operations.</p>
  </div>
  <div style="left:120px;top:158px;width:.5px;height:50px;background:var(--rule)"></div>
  <h2 class="head" style="left:136px;top:159px"><b>Education</b></h2>
  <div class="copy" style="left:136px;top:182px;width:82px;color:#5d6774">
    <p>QTS delivers innovative AV solutions for schools, universities, and training institutions including lecture theatres, classrooms, hybrid learning environments, school halls, gymnasiums, and large-scale LED display systems.</p>
  </div>
  <p class="footer" style="left:0;width:240px;text-align:center;top:219px;color:#5d6774">www.quorintech.com.au</p>
</section>

<!-- Spread 2 right: feature image -->
<section class="page" style="left:332px;top:305px;background:#1b1b1b">
  <div class="photo console" role="img" aria-label="Close view of an audio mixing console with faders and knobs" style="left:0;top:0;width:241px;height:240px"></div>
  <div style="left:0;top:59px;width:241px;height:59px;background:rgba(24,26,30,.92)"></div>
  <h2 class="display" style="left:0;top:66px;width:241px">Connecting People<br>With Technology</h2>
  <p class="footer" style="left:0;width:241px;text-align:center;top:219px;color:#d0d0d0">quorin tech</p>
</section>

<!-- Spread 3 left: design and implementation -->
<section class="page light" style="left:630px;top:305px">
  <h2 class="head" style="left:23px;top:25px"><b>Design &amp;</b><br>Engineering</h2>
  <div class="copy" style="left:77px;top:24px;width:141px">
    <p>QTS provides comprehensive in-house design and engineering services including system architecture, documentation, schematics, networked AV design, and integration with existing IT infrastructure.</p>
    <p>Our team works closely with architects, consultants, builders, and project managers to ensure seamless integration of audiovisual technology within new builds and refurbishment projects.</p>
  </div>
  <div class="photo" role="img" aria-label="Tiered lecture theatre with rows of seats facing a screen" style="left:0;top:71px;width:240px;height:43px"></div>
  <h2 class="head" style="left:0;width:240px;text-align:center;top:140px"><b>Implementation</b><br>&amp; Commissioning</h2>
  <div class="copy" style="left:25px;top:169px;width:193px">
    <p>QTS delivers complete turnkey project implementation including equipment procurement, professional installation, system configuration, testing, commissioning, and user training.</p>
    <p>Our accredited technicians ensure systems are delivered safely, efficiently, and with minimal disruption to operational environments.</p>
  </div>
  <p class="footer" style="left:0;width:240px;text-align:center;top:219px;color:#3a3d42">quorin tech</p>
  <div class="wordmark" style="left:187px;top:213px;color:#55585c">quorin tech</div>
</section>

<!-- Spread 3 right: service, governance, why choose -->
<section class="page dark" style="left:870px;top:305px">
  <h2 class="head" style="left:23px;top:25px"><b>Service</b><br>&amp; Support</h2>
  <div class="copy" style="left:85px;top:24px;width:133px;color:#5d6774">
    <p>QTS provides comprehensive ongoing support services including preventative maintenance, priority service response, remote diagnostics, system upgrades, and technology lifecycle planning.</p>
    <p>Our long-term support partnerships ensure systems remain reliable, secure, and aligned with evolving organisational needs.</p>
  </div>
  <div class="rule" style="left:23px;top:62px;width:193px"></div>
  <h2 class="head" style="left:23px;top:83px"><b>Governance,</b><br>Safety<br><b>&amp; Compliance</b></h2>
  <div class="copy" style="left:86px;top:81px;width:132px;color:#5d6774">
    <p>QTS operates under strict safety and governance frameworks including OH&amp;S compliant work practices, industry-certified technicians, and full public liability and professional indemnity coverage.</p>
    <p>Safety, compliance, and quality assurance are embedded throughout all project delivery activities.</p>
  </div>
  <div class="rule" style="left:23px;top:124px;width:193px"></div>
  <h2 class="head" style="left:87px;top:143px"><b>Why Choose</b><br>Quorin Tech Systems</h2>
  <ul class="market-list" style="left:23px;top:170px;font-size:3.5px;line-height:2.3;color:#6c7784">
    <li>26+ Years Audiovisual Integration Experience.</li>
    <li>Proven Track Record Across Multiple Industries.</li>
    <li>In-House Design &amp; Engineering Capability.</li>
  </ul>
  <ul class="market-list" style="left:129px;top:170px;font-size:3.5px;line-height:2.3;color:#6c7784">
    <li>National Project Delivery Capability.</li>
    <li>Led Video Wall Specialists.</li>
    <li>Long-Term Service &amp; Support Partnerships.</li>
  </ul>
  <p class="footer" style="left:0;width:160px;text-align:center;top:219px;color:#5d6774">www.quorintech.com.au</p>
  <div class="wordmark" style="left:187px;top:213px">quorin tech</div>
</section>

<!-- Back cover -->
<section class="page back" style="left:481px;top:570px;width:241px;background:var(--navy)">
  <div style="left:62px;top:109px;width:14px;height:14px;background:#b9bec4"></div>
  <div class="wordmark" style="left:82px;top:107px;font-size:9px;color:#e6eaee">quorin tech</div>
  <p style="left:82px;top:122px;font-size:3.2px;color:#dfe5ec;letter-spacing:.1px">CONNECTING PEOPLE WITH TECHNOLOGY</p>
  <div class="rule" style="left:136px;top:210px;width:84px;background:#4f6e92"></div>
  <p class="footer" style="right:20px;top:216px;color:#c7d1dc">www.quorintech.com.au</p>
</section>

</body>
</html>
```